Maple Ridge business card design

Card needs to include the following text/items:
Company Logo
Tobin Marsh
Phone # - 555-318-7642
service@mapleridgelandscaping.example
Lawn & landscape maintenance services

```html
<!DOCTYPE html>
<html lang="en">
<head>
<meta charset="utf-8">
<title>Maple Ridge Landscaping – Business Card</title>
<link rel="stylesheet" href="https://fonts.googleapis.com/css2?family=Raleway:wght@400;500;700;800&display=swap">
<style>
  :root {
    --page-bg: #e9e9ea;
    --card-center: #3b3a3c;
    --card-edge: #1b191a;
    --text-light: #f2f2f2;
    --text-muted: #d6d6d6;
    --brand-green: #1f9a4a;
    --badge-ring: #6f7d35;
    --rule: #8a8a8a;
  }
  * { box-sizing: border-box; margin: 0; padding: 0; }
  html, body {
    width: 672px;
    height: 1200px;
    overflow: hidden;
    background: var(--page-bg);
  }
  .sheet {
    width: 672px;
    height: 1200px;
    display: flex;
    flex-direction: column;
    align-items: center;
    justify-content: center;
    gap: 56px;
  }
  .card {
    width: 560px;
    height: 320px;
    background: radial-gradient(ellipse 60% 70% at 50% 45%, var(--card-center) 0%, var(--card-edge) 100%);
    box-shadow: 0 14px 22px -10px rgba(0,0,0,0.35);
    display: flex;
    flex-direction: column;
    align-items: center;
    font-family: "Raleway", sans-serif;
    color: var(--text-light);
  }

  /* Front */
  .card--front { justify-content: flex-start; padding-top: 84px; }
  .brand-mark {
    display: flex;
    align-items: center;
    gap: 12px;
  }
  .brand-mark__dot {
    width: 44px;
    height: 44px;
    border-radius: 50%;
    background: var(--badge-ring);
  }
  .brand-mark__name {
    font-weight: 700;
    font-size: 30px;
    letter-spacing: 0.5px;
    color: var(--text-light);
  }
  .card--front .web {
    margin-top: 106px;
    font-size: 13px;
    letter-spacing: 1.6px;
    color: var(--text-muted);
  }

  /* Back */
  .card--back { justify-content: flex-start; padding-top: 52px; }
  .card--back .brand-mark__dot { width: 36px; height: 36px; }
  .card--back .brand-mark__name { font-size: 24px; }
  .holder-name {
    margin-top: 22px;
    font-weight: 800;
    font-size: 21px;
    letter-spacing: -0.3px;
  }
  .holder-role {
    margin-top: 4px;
    font-weight: 500;
    font-size: 14.5px;
    line-height: 16px;
    text-align: center;
    color: var(--brand-green);
  }
  .divider {
    width: 143px;
    height: 1px;
    margin-top: 18px;
    background: var(--rule);
  }
  .contacts {
    margin-top: 14px;
    display: flex;
    flex-direction: column;
    align-items: center;
    gap: 6px;
    font-size: 12.5px;
    font-weight: 500;
  }
  .contact {
    display: flex;
    align-items: center;
    gap: 14px;
  }
  .contact svg { fill: var(--brand-green); }
</style>
</head>
<body>
<main class="sheet">
  <section class="card card--front" aria-label="Card front">
    <div class="brand-mark">
      <span class="brand-mark__dot"></span>
      <span class="brand-mark__name">Maple Ridge</span>
    </div>
    <p class="web">www.mapleridgelandscaping.example</p>
  </section>

  <section class="card card--back" aria-label="Card back">
    <div class="brand-mark">
      <span class="brand-mark__dot"></span>
      <span class="brand-mark__name">Maple Ridge</span>
    </div>
    <h1 class="holder-name">Tobin Marsh</h1>
    <p class="holder-role">Lawn &amp; Landscape<br>Maintenance Services</p>
    <div class="divider"></div>
    <div class="contacts">
      <div class="contact">
        <svg width="12" height="12" viewBox="0 0 24 24" aria-hidden="true"><path d="M6.6 10.8a15.1 15.1 0 0 0 6.6 6.6l2.2-2.2a1 1 0 0 1 1-.25 11.4 11.4 0 0 0 3.6.57 1 1 0 0 1 1 1V20a1 1 0 0 1-1 1A17 17 0 0 1 3 4a1 1 0 0 1 1-1h3.5a1 1 0 0 1 1 1c0 1.25.2 2.45.57 3.57a1 1 0 0 1-.25 1z"/></svg>
        <span>555-318-7642</span>
      </div>
      <div class="contact">
        <svg width="12" height="10" viewBox="0 0 24 18" aria-hidden="true"><path d="M0 2v14h24V2L12 10z"/><path d="M0 0h24L12 8z"/></svg>
        <span>service@mapleridgelandscaping.example</span>
      </div>
    </div>
  </section>
</main>
</body>
</html>
```